Corwenna Foundation is a new grant making charity set up in the UK.

Having got a logo, we now need a website to go with it. We have worked out the text which people are going to need in order to then apply for grants. But having found out what we require they will probably need to go away and think about it.
We have to be careful of what images we use. So I have uploaded some images that we like. We are also going to be adding more pages almost immediately so need to think about the images for these.
I know basic wordpress so I will be able to add new pages/make alterations in future.
Updates
The website does need to be coded in Wordpress so that I can maintain it afterwards.
Corwenna
Brief changed to provide more money and we have also provided more possible pictures. And generally more explanation.
Target Market(s)
departments in universities, other charities doing work on relief of pain, people working in health service departments
Industry/Entity Type
Health Charity
Coding
Coded - Design and coding required
Number of Pages Required
4 page
Look and feel
Each slider illustrates characteristics of the customer's brand and the style your logo design should communicate.

```html
<!DOCTYPE html>
<html lang="en">
<head>
<meta charset="utf-8">
<title>Corwenna Foundation</title>
<link href="https://fonts.googleapis.com/css2?family=Lexend+Exa:wght@500;600;700&family=Poppins:wght@400;500;600&display=swap" rel="stylesheet">
<style>
:root{
  --blue:#0f6fc6;
  --blue-dark:#0a4f9a;
  --navy:#0b1f4a;
  --ink:#222;
  --grey:#777;
  --frame:#c4c4c4;
  --field:#f7f8fb;
  --contact-bg:#7d7d7d;
  --white:#fff;
}
*{margin:0;padding:0;box-sizing:border-box}
html,body{width:1200px;height:3026px;overflow:hidden;background:var(--white)}
body{position:relative;font-family:"Poppins",sans-serif;color:var(--ink)}
.abs{position:absolute}
.display{font-family:"Lexend Exa",sans-serif}

/* header */
.site-header{left:0;top:0;width:1200px;height:80px;background:var(--white)}
.brand{display:flex;align-items:center;gap:8px}
.brand-mark{width:22px;height:22px;background:var(--blue)}
.brand-name{font-family:"Lexend Exa",sans-serif;font-weight:600;color:var(--blue);line-height:1.05;letter-spacing:.5px}
.site-header .brand{left:132px;top:18px}
.site-header .brand-name{font-size:15px}
.main-nav a{position:absolute;top:24px;font-family:"Lexend Exa",sans-serif;font-size:13px;font-weight:500;color:#333;text-decoration:none;letter-spacing:.3px}
.main-nav .active{color:var(--blue)}
.main-nav .active::after{content:"";position:absolute;left:-2px;right:-2px;top:29px;height:3px;background:var(--blue)}

/* hero */
.hero{left:0;top:80px;width:1200px;height:635px;background:radial-gradient(circle at 75% 40%,#3c6fd0 0%,#1a3d8f 30%,#0b1f4a 65%,#081430 100%)}
.hero-title{left:122px;top:178px;font-size:48px;font-weight:700;color:var(--white);line-height:1.12;letter-spacing:1px}
.hero-tag{left:122px;top:292px;font-size:21px;font-weight:600;color:var(--white);line-height:1.45;letter-spacing:.5px}
.btn{position:absolute;display:flex;align-items:center;justify-content:center;font-family:"Lexend Exa",sans-serif;font-size:13px;font-weight:600;text-decoration:none}
.hero .btn-outline{left:130px;top:376px;width:156px;height:46px;border:2px solid var(--white);color:var(--white)}
.hero .btn-solid{left:293px;top:376px;width:156px;height:46px;background:var(--blue);color:var(--white)}
.slider-arrow{position:absolute;top:265px;width:40px;height:40px;border-radius:50%;background:var(--white)}
.slider-arrow.prev{left:28px}
.slider-arrow.next{left:1132px}

/* about */
.about-visual{left:143px;top:797px;width:403px;height:385px;border:2px solid var(--blue);padding:10px}
.about-visual .fill{width:100%;height:100%;background:linear-gradient(180deg,#fff 0%,#fff 35%,#c9553f 60%,#9b2b3a 100%)}
.bracket{position:absolute;border:3px solid var(--frame)}
.about-frame{left:966px;top:772px;width:144px;height:418px;border-left:none}
.about-frame-tl{left:964px;top:772px;width:3px;height:32px;background:var(--frame)}
.about-frame-bl{left:964px;top:1145px;width:3px;height:45px;background:var(--frame)}
.about-heading{left:626px;top:836px;font-size:29px;font-weight:700;line-height:1.25;color:var(--blue);letter-spacing:.5px}
.about-heading span{color:#666;font-weight:500}
.rule{position:absolute;height:3px;background:var(--blue)}
.about-text{left:626px;top:940px;width:460px;font-size:16.5px;line-height:29px;color:#333}
.about-text p+p{margin-top:18px}
.btn-pill-outline{left:621px;top:1097px;width:143px;height:41px;border:2px solid var(--blue);border-radius:22px;color:var(--blue);font-size:12px}

/* grants */
.grants{left:0;top:1252px;width:1200px;height:533px;background:radial-gradient(circle at 75% 45%,#2a6fe0 0%,#1848a8 35%,#0c2a6e 70%,#071a47 100%)}
.grants-bracket{left:94px;top:53px;width:144px;height:419px;border:3px solid var(--blue);border-right:none}
.grants-bracket-tr{left:235px;top:53px;width:3px;height:30px;background:var(--blue)}
.grants-bracket-br{left:235px;top:427px;width:3px;height:45px;background:var(--blue)}
.grants-heading{left:138px;top:123px;font-size:29px;font-weight:600;color:var(--white);letter-spacing:.5px}
.grants-text{left:137px;top:192px;width:400px;font-size:14.3px;line-height:19px;color:var(--white)}
.grants-text p+p{margin-top:17px}
.btn-pill-white{left:137px;top:349px;width:154px;height:44px;border-radius:22px;background:var(--white);color:var(--blue);font-size:12.5px}

/* faq */
.faq{left:0;top:1785px;width:1200px;height:585px;background:linear-gradient(180deg,#f3f4f6,#fbfbfc 60%,#f4f5f7)}
.faq-heading{left:0;width:1200px;top:58px;text-align:center;font-size:28px;font-weight:700;color:var(--blue)}
.faq-item{position:absolute;left:154px;width:853px;height:57px;border:1px solid #bdbdbd;background:rgba(255,255,255,.55);padding:0 28px;display:flex;align-items:center;font-family:"Lexend Exa",sans-serif;font-size:12.5px;font-weight:600;color:#222}
.faq-item.open{display:block;height:143px;border-color:var(--blue);padding-top:20px}
.faq-answer{margin-top:22px;width:700px;font-family:"Poppins",sans-serif;font-size:13.5px;font-weight:400;line-height:18.5px;color:#444}

/* contact */
.contact{left:0;top:2370px;width:1200px;height:435px;background:radial-gradient(circle at 50% 50%,#8c8c8c,#707070)}
.contact-heading{left:0;width:1200px;top:73px;text-align:center;font-size:27px;font-weight:600;color:var(--white);letter-spacing:.5px}
.field{position:absolute;background:var(--field);display:flex;align-items:center;gap:12px;padding-left:18px;font-size:13px;color:#444}
.field svg{width:16px;height:16px}
.field.message{align-items:flex-start;padding-top:16px;padding-left:22px}
.btn-submit{left:517px;top:335px;width:172px;height:44px;border-radius:22px;background:var(--blue);color:var(--white);font-size:15px;font-family:"Poppins",sans-serif;letter-spacing:1px}

/* footer */
.site-footer .brand{left:0;width:1200px;top:2848px;justify-content:center}
.site-footer .brand-name{font-size:22px}
.site-footer .brand-mark{width:30px;height:30px}
.footer-nav a{position:absolute;top:2925px;font-family:"Lexend Exa",sans-serif;font-size:14px;font-weight:500;color:#222;text-decoration:none}
.copyright{left:0;width:1200px;top:2966px;text-align:center;font-size:11.5px;color:#444}
</style>
</head>
<body>

<header class="site-header abs">
  <div class="brand abs"><span class="brand-mark"></span><span class="brand-name">CORWENNA<br>FOUNDATION</span></div>
  <nav class="main-nav">
    <a class="active" style="left:537px" href="#">HOME</a>
    <a style="left:653px" href="#">ABOUT US</a>
    <a style="left:802px" href="#">GRANTS</a>
    <a style="left:936px" href="#">CONTACT US</a>
  </nav>
</header>

<section class="hero abs" role="img" aria-label="Close-up photograph of a glowing blue neuron with orange light points">
  <h1 class="hero-title abs display">CORWENNA<br>FOUNDATION</h1>
  <p class="hero-tag abs display">WE REDUCE THE SUFFERING<br>CAUSED BY CHRONIC PAIN.</p>
  <a class="btn btn-outline" href="#">CONTACT US</a>
  <a class="btn btn-solid" href="#">LEARN MORE</a>
  <span class="slider-arrow prev"><svg width="40" height="40" viewBox="0 0 40 40"><path d="M23 13l-7 7 7 7" fill="none" stroke="#111" stroke-width="3" stroke-linecap="round" stroke-linejoin="round"/></svg></span>
  <span class="slider-arrow next"><svg width="40" height="40" viewBox="0 0 40 40"><path d="M17 13l7 7-7 7" fill="none" stroke="#111" stroke-width="3" stroke-linecap="round" stroke-linejoin="round"/></svg></span>
</section>

<section class="about">
  <div class="about-visual abs"><div class="fill" role="img" aria-label="Illustration of a colourful crowd of people under the foundation name"></div></div>
  <div class="bracket about-frame"></div>
  <div class="about-frame-tl abs"></div>
  <div class="about-frame-bl abs"></div>
  <h2 class="about-heading abs display">ABOUT CORWENNA<br><span>FOUNDATION</span></h2>
  <div class="rule" style="left:627px;top:916px;width:63px"></div>
  <div class="about-text abs">
    <p>Corwenna Foundation is a grant making charity set up in the UK in 2021. The main aim of Corwenna Foundation is to reduce the suffering caused by chronic pain.</p>
    <p>Charity registration number 1187654.</p>
  </div>
  <a class="btn btn-pill-outline" href="#">LEARN MORE</a>
</section>

<section class="grants abs" role="img" aria-label="Photograph of blue neurons connected by glowing fibres">
  <div class="bracket grants-bracket"></div>
  <div class="grants-bracket-tr abs"></div>
  <div class="grants-bracket-br abs"></div>
  <h2 class="grants-heading abs display">CORWENNA GRANTS</h2>
  <div class="rule" style="left:139px;top:167px;width:60px;background:#fff"></div>
  <div class="grants-text abs">
    <p>Grants will almost entirely be provided for research or education into pain management, or the prevention of pain.</p>
    <p>The trustees will also be providing grants to a number of other charities or to areas with which they have had a long term association such as HIV/AIDS and TB. There is no application procedure for these other areas</p>
  </div>
  <a class="btn btn-pill-white" href="#">LEARN MORE</a>
</section>

<section class="faq abs">
  <h2 class="faq-heading abs display">FAQ</h2>
  <div class="rule" style="left:553px;top:99px;width:68px"></div>
  <div class="faq-item" style="top:129px">WHO ARE THE TRUSTEES OF CORWENNA FOUNDATION?</div>
  <div class="faq-item" style="top:201px">WHO ARE THE MEDICAL ADVISERS TO CORWENNA FOUNDATION?</div>
  <div class="faq-item" style="top:275px">HOW MUCH MONEY DOES CORWENNA FOUNDATION HAVE?</div>
  <div class="faq-item open" style="top:347px">WHERE HAS THIS MONEY COME FROM?
    <p class="faq-answer">The million pounds has been inherited from Corwenna’s father, the late Sir Robert Hallworth, who had a large stake in the Hallworth supermarket business. Further significant money is going to come from the sale of the farm where the Penrose family currently live.</p>
  </div>
</section>

<section class="contact abs" role="img" aria-label="Faint grey network of neural fibres">
  <h2 class="contact-heading abs display">CONTACT CORWENNA</h2>
  <div class="rule" style="left:565px;top:112px;width:70px;background:#fff"></div>
  <div class="field" style="left:194px;top:145px;width:401px;height:48px">
    <svg viewBox="0 0 16 16"><circle cx="8" cy="5" r="3.2" fill="none" stroke="#555" stroke-width="1.3"/><path d="M2.5 15c0-3.5 2.5-5.5 5.5-5.5s5.5 2 5.5 5.5" fill="none" stroke="#555" stroke-width="1.3"/></svg>Name</div>
  <div class="field" style="left:194px;top:201px;width:401px;height:48px">
    <svg viewBox="0 0 16 16"><rect x="1.5" y="3.5" width="13" height="9" fill="none" stroke="#555" stroke-width="1.3"/><path d="M1.5 3.5l6.5 5 6.5-5" fill="none" stroke="#555" stroke-width="1.3"/></svg>E-mail address</div>
  <div class="field" style="left:194px;top:257px;width:401px;height:48px">
    <svg viewBox="0 0 16 16"><path d="M4 1.5l2.5 3-1.5 2c1 2 2.5 3.5 4.5 4.5l2-1.5 3 2.5-1.5 2.5C7 14 2 9 1.5 3z" fill="#2f5fa0"/></svg>Phone</div>
  <div class="field message" style="left:604px;top:145px;width:399px;height:161px">Message</div>
  <a class="btn btn-submit" href="#">SUBMIT</a>
</section>

<footer class="site-footer">
  <div class="brand abs"><span class="brand-mark"></span><span class="brand-name">CORWENNA FOUNDATION</span></div>
  <nav class="footer-nav">
    <a style="left:314px" href="#">HOME</a>
    <a style="left:436px" href="#">ABOUT US</a>
    <a style="left:594px" href="#">GRANTS</a>
    <a style="left:736px" href="#">CONTACT US</a>
  </nav>
  <p class="copyright abs">Copyright © 2021 Corwenna Foundation &nbsp;|&nbsp; All Rights Reserved</p>
</footer>

</body>
</html>
```